Leadership Development Booklet

Design a booklet to be used in a training course on leadership development. The training material is provided in the word doc, but need to enhance the look.

Target Market(s)

Executive Managers

Industry/Entity Type

Water Industry

Font styles to use
Other font styles liked:
• Helvetica

Colors
0054AA
0677BA
7BADD7
CADEEF
E8F1F8

```html
<!DOCTYPE html>
<html lang="en">
<head>
<meta charset="utf-8">
<title>Navira Leadership Development Booklet</title>
<link href="https://fonts.googleapis.com/css2?family=Arimo:wght@400;700&family=Roboto+Condensed:wght@400;700&display=swap" rel="stylesheet">
<style>
:root{
  --navy:#1f3a9e;
  --blue:#0054AA;
  --mid:#0677BA;
  --sky:#7BADD7;
  --pale:#CADEEF;
  --mist:#E8F1F8;
  --row:#e6eaf5;
  --ink:#333;
  --bg:#c9c9c9;
}
*{box-sizing:border-box;margin:0;padding:0}
html,body{width:1200px;height:3012px;overflow:hidden;background:var(--bg);font-family:Arimo,Helvetica,Arial,sans-serif;color:var(--ink)}
.canvas{position:relative;width:1200px;height:3012px}
.page{position:absolute;width:328px;height:427px;background:#fff;overflow:hidden;box-shadow:0 1px 3px rgba(0,0,0,.15)}
.brand{position:absolute;left:22px;bottom:18px;font:700 22px "Roboto Condensed",sans-serif;color:var(--navy);letter-spacing:.5px}
.pg{position:absolute;right:22px;bottom:22px;width:15px;height:15px;border:1px solid var(--sky);border-radius:50%;font-size:5.5px;color:var(--blue);display:flex;align-items:center;justify-content:center}
.tag{position:absolute;left:20px;top:20px;background:var(--navy);color:#fff;font:700 13px "Roboto Condensed",sans-serif;padding:1px 10px 1px 6px;border-radius:0 8px 0 0}
.sub{position:absolute;left:20px;top:38px;right:20px;font:700 8px "Roboto Condensed",sans-serif;color:var(--navy)}
.lede{position:absolute;left:20px;right:20px;font-size:4.6px;line-height:1.4;color:#555}
.title{position:absolute;left:20px;top:25px;right:20px;font:700 9.5px "Roboto Condensed",sans-serif;color:var(--navy)}
.n{background:var(--navy);color:#fff;font:700 7px Arimo,sans-serif;display:flex;align-items:center;justify-content:center}
.ph{background:linear-gradient(160deg,#8ea3c9,#3a4f86)}
.tiny{font-size:4.2px;line-height:1.45;color:#555}
/* cover */
.cover{background:linear-gradient(180deg,#3048b8 0%,var(--navy) 60%,#17307f 100%)}
.cover .stripe{position:absolute;left:0;top:0;width:18px;height:100%;background:#2a45b5}
.cover .hero{position:absolute;left:72px;top:78px;width:184px;height:200px;clip-path:polygon(50% 0,100% 25%,100% 75%,50% 100%,0 75%,0 25%);background:linear-gradient(180deg,#6f86b8,#c9b79a 55%,#5d6f9a)}
.cover .mark{position:absolute;top:18px;left:0;right:0;text-align:center;font:700 30px "Roboto Condensed",sans-serif;color:#fff}
.cover h1{position:absolute;top:310px;left:0;right:0;text-align:center;font:700 27px/1 "Roboto Condensed",sans-serif;color:#fff}
.cover p{position:absolute;top:372px;left:40px;right:40px;text-align:center;font-size:10.5px;line-height:1.3;color:#fff}
/* values */
.values{position:absolute;left:24px;right:24px;top:35px;height:62px;border:1.5px solid var(--navy);border-radius:4px}
.values .vt{position:absolute;top:-9px;left:50%;transform:translateX(-50%);background:#fff;border:1.5px solid var(--navy);border-radius:9px;padding:1px 10px;font:700 12px "Roboto Condensed",sans-serif;color:var(--navy);white-space:nowrap}
.vals{position:absolute;top:14px;left:4px;right:4px;display:flex;justify-content:space-around}
.val{width:44px;text-align:center;font:700 6px Arimo,sans-serif;color:var(--navy)}
.val i{display:block;width:30px;height:30px;margin:0 auto 3px;border-radius:50%;border:2px solid var(--sky);background:var(--mist);position:relative}
.val i:after{content:"";position:absolute;inset:8px;border-radius:50%;background:var(--navy)}
.promises{position:absolute;left:22px;right:22px;top:130px;height:232px;background:var(--navy);padding:5px 6px;color:#fff}
.promises h3{font:700 9px "Roboto Condensed",sans-serif}
.promises .pi{font-size:3.6px;opacity:.8;margin-bottom:3px}
.prom{display:flex;gap:5px;border-top:1px solid rgba(255,255,255,.35);padding:3px 0;height:26px}
.prom b{background:#fff;color:var(--navy);font-size:5px;width:10px;height:9px;display:flex;align-items:center;justify-content:center;flex:none}
.prom strong{display:block;font-size:5.6px}
.prom span{font-size:3.4px;opacity:.8;line-height:1.3}
/* module */
.modhead{position:absolute;left:0;right:0;top:0;height:128px;background:var(--navy);color:#fff;padding:16px 22px}
.modhead h2{font:700 19px "Roboto Condensed",sans-serif}
.modhead q{display:block;margin-top:14px;font:700 5.6px/1.4 Arimo,sans-serif;quotes:none}
.modhead cite{display:block;margin-top:6px;text-align:center;font-size:5.2px;font-style:italic}
.lo{position:absolute;top:118px;left:50%;transform:translateX(-50%);background:#fff;padding:2px 10px;font:700 11px "Roboto Condensed",sans-serif;color:var(--navy);white-space:nowrap;border-radius:4px 4px 0 0}
.locards{position:absolute;top:142px;left:34px;right:34px;display:grid;grid-template-columns:repeat(3,1fr);gap:14px 12px}
.loc{height:88px;border:1px solid #c8c8c8;border-radius:3px;text-align:center;font:700 6px/1.3 Arimo,sans-serif;color:var(--navy);padding-top:48px;position:relative}
.loc:before{content:"";position:absolute;top:-4px;left:50%;transform:translateX(-50%);width:38px;height:42px;background:var(--navy);clip-path:polygon(50% 0,100% 25%,100% 75%,50% 100%,0 75%,0 25%)}
.loc:after{content:"";position:absolute;top:9px;left:50%;transform:translateX(-50%);width:16px;height:16px;border:2px solid #fff;border-radius:50%}
/* tables */
.t1{position:absolute;left:22px;right:22px;top:88px}
.t1 .hd{margin-left:30px;width:180px;background:var(--navy);color:#fff;font:700 5.6px Arimo,sans-serif;padding:4px 12px;border-radius:0 8px 0 0}
.t1 .r{display:flex;height:43px;border-bottom:1px solid #fff}
.t1 .r .n{width:28px}
.t1 .r div:last-child{flex:1;background:var(--row)}
.t1 .r:nth-child(even) div:last-child{background:#f4f5fa}
.t2{position:absolute;left:22px;right:22px;top:78px}
.t2 .hd,.t2 .r{display:grid;grid-template-columns:12px 40px 1fr 40px 24px}
.t2 .hd div{background:var(--navy);color:#fff;font-size:4.3px;height:13px;display:flex;align-items:center;justify-content:center;text-align:center;border-right:1px solid #fff}
.t2 .hd .e{background:none}
.t2 .r{height:18.5px;border-bottom:1px solid #d3d8e8}
.t2 .r div{font-size:3.8px;color:#444;display:flex;align-items:center;padding-left:3px;border-right:1px solid #d3d8e8}
.t2 .r .n{font-size:4.5px;padding:0;justify-content:center;border-right:none}
.t2 .r:nth-child(even){background:var(--row)}
.refl{position:absolute;left:22px;right:22px;display:flex}
.refl .n{width:22px;height:22px;border-radius:0 10px 10px 0;margin-top:12px;flex:none}
.refl .box{flex:1;height:56px;background:var(--row);font-size:4.6px;color:#444;padding:4px 6px}
.refl.w .box{background:#fff}
/* exercise 4 */
.ex4row{position:absolute;left:20px;right:20px;display:flex;gap:4px}
.ex4row .n{width:12px;height:11px;font-size:5px;flex:none}
.ex4row b{display:block;font-size:4.6px;color:var(--navy)}
.band{position:absolute;left:20px;width:100px;height:8px;background:var(--navy);color:#fff;font-size:4px;padding:2px 4px}
/* list page */
.listhd{position:absolute;left:26px;right:26px;top:22px;background:var(--navy);color:#fff;font:700 6px Arimo,sans-serif;padding:4px 10px;border-radius:0 8px 0 0}
.list{position:absolute;left:22px;right:26px;top:38px}
.list div{display:flex;align-items:center;gap:6px;height:18.6px;border-bottom:1px solid #ccd;font-size:4.8px;color:#444}
.list .n{width:10px;height:12px;font-size:4.5px;flex:none}
/* ex5 */
.t5{position:absolute;left:20px;right:20px;top:82px}
.t5 .hd,.t5 .r{display:grid;grid-template-columns:22px 106px 50px 1fr}
.t5 .hd div{background:var(--navy);color:#fff;font:700 4.8px Arimo,sans-serif;height:16px;display:flex;align-items:center;justify-content:center;border-right:1px solid #fff}
.t5 .hd .e{background:none}
.t5 .r{height:42px}
.t5 .r div{border-right:1px solid #ccd;border-bottom:1px solid #ccd}
.t5 .r .n{border-radius:0 10px 10px 0;height:28px;align-self:center;border:none}
/* steps */
.steps{position:absolute;left:20px;right:20px;top:86px}
.steps .hd{margin-left:20px;background:var(--navy);color:#fff;font:700 8px "Roboto Condensed",sans-serif;padding:3px 8px;border-radius:0 8px 0 0}
.step{display:flex;border-bottom:1px solid #fff}
.step .n{width:20px;flex:none;font-size:8px}
.step div:last-child{flex:1;background:var(--row);padding:5px 6px;font-size:4px;line-height:1.4;color:#444}
.step:nth-child(odd) div:last-child{background:#f4f5fa}
.step strong{display:block;font-size:6.6px;color:var(--navy);margin-bottom:2px}
/* styles table */
.t11{position:absolute;left:22px;right:22px;top:88px}
.t11 .hd,.t11 .r{display:grid;grid-template-columns:40px 1fr 1fr}
.t11 .hd div{background:var(--navy);color:#fff;font:700 4.8px Arimo,sans-serif;height:12px;display:flex;align-items:center;justify-content:center;border-right:2px solid #fff;border-radius:0 6px 0 0}
.t11 .r{height:41px;border-bottom:1px solid #fff}
.t11 .r div{display:flex;align-items:center;padding:0 8px;font-size:4.2px;line-height:1.35;color:#333}
.t11 .r .term{background:var(--navy);color:#fff;font-weight:700;font-size:4.3px;padding:0 4px}
.t11 .r div:nth-child(2){background:var(--row)}
.t11 .r div:nth-child(3){background:#f4f5fa}
/* article */
.art{position:absolute;left:22px;right:22px}
.bul div{font-size:3.8px;color:#333;padding:3px 0 3px 10px;border-bottom:1px solid #ddd;position:relative;font-weight:700}
.bul div:before{content:"";position:absolute;left:2px;top:3px;width:4px;height:4px;border:1px solid var(--blue);border-radius:50%}
/* quadrant pages */
.qtitle{position:absolute;left:0;right:0;top:26px;text-align:center;font:700 8px Arimo,sans-serif;color:#333}
.axis{position:absolute;font:700 4.4px Arimo,sans-serif;color:var(--navy);white-space:nowrap}
.quad{position:absolute;left:44px;right:44px;top:74px;height:268px;display:grid;grid-template-columns:1fr 1fr;gap:14px 12px}
.quad:before{content:"";position:absolute;left:50%;top:-4px;bottom:-4px;width:1.5px;background:var(--navy)}
.quad:after{content:"";position:absolute;top:50%;left:-6px;right:-6px;height:1.5px;background:var(--navy)}
.q{border:1px solid #9fb0d6;background:#fff;position:relative;z-index:1;text-align:center}
.q h4{background:var(--navy);color:#fff;font:700 4.4px Arimo,sans-serif;padding:2px 0}
.q p{font-size:3.6px;line-height:1.5;color:var(--mid);padding:1px 4px}
.q p.k{color:#555}
/* back cover */
.back{background:linear-gradient(180deg,#3550c2,var(--navy) 60%,#1b3490)}
.back .house{position:absolute;left:74px;bottom:0;width:180px;height:112px;background:#fff;clip-path:polygon(50% 0,100% 26%,100% 100%,0 100%,0 26%)}
.back .hm{position:absolute;left:74px;width:180px;text-align:center;color:var(--navy);font-family:"Roboto Condensed",sans-serif;font-weight:700}
</style>
</head>
<body>
<div class="canvas">

<!-- 1 cover -->
<section class="page cover" style="left:82px;top:98px">
  <div class="stripe"></div>
  <div class="mark">NAVIRA</div>
  <div class="hero" role="img" aria-label="Silhouettes of three people on a mountain top, one raising a trophy, against a sunset sky"></div>
  <h1>LEADERSHIP<br>DEVELOPMENT</h1>
  <p>Developing Navira's greatest resource and most valuable assets- our people.</p>
</section>

<!-- 2 values -->
<section class="page" style="left:441px;top:98px">
  <div class="values">
    <div class="vt">NAVIRA VALUES</div>
    <div class="vals">
      <div class="val"><i></i>Quality</div>
      <div class="val"><i></i>Sustainability</div>
      <div class="val"><i></i>Reliability</div>
      <div class="val"><i></i>Innovation</div>
      <div class="val"><i></i>Customer Service</div>
    </div>
  </div>
  <div class="promises">
    <h3>CUSTOMER PROMISES</h3>
    <div class="pi">Our unique selling propositions enable us to give eight important promises to our customers:</div>
    <div class="prom"><b>01</b><div><strong>EXPECT SOLUTIONS, NOT JUST PRODUCTS</strong><span>It takes dedicated expertise to choose the right solution so that customers get the best quality.</span></div></div>
    <div class="prom"><b>02</b><div><strong>EXPECT GLOBAL LEADERSHIP AND LOCAL COMMITMENT</strong><span>Customers expect a partner who combines product portfolio with local knowledge.</span></div></div>
    <div class="prom"><b>03</b><div><strong>EXPECT QUALITY IN EVERY STEP</strong><span>Quality is essential when it comes to valves, hydrants, fittings and accessories.</span></div></div>
    <div class="prom"><b>04</b><div><strong>EXPECT PROMPT RESPONSE</strong><span>From the customer's perspective our service and offerings form part of complex installations.</span></div></div>
    <div class="prom"><b>05</b><div><strong>EXPECT LASTING INNOVATIONS</strong><span>To stand out from the competition it is essential to keep offering innovative solutions.</span></div></div>
    <div class="prom"><b>06</b><div><strong>EXPECT TOTAL SAVINGS</strong><span>For many of our customers it is important that we optimise our solutions.</span></div></div>
    <div class="prom"><b>07</b><div><strong>EXPECT A LONG-TERM PARTNERSHIP</strong><span>We build on and invest in long-term partnerships with our customers.</span></div></div>
    <div class="prom"><b>08</b><div><strong>EXPECT IT TO BE EFFECTIVE AND EASY</strong><span>Our customers need a business partner who is easy to do business with.</span></div></div>
  </div>
  <div class="brand">NAVIRA</div><div class="pg">02</div>
</section>

<!-- 3 module -->
<section class="page" style="left:795px;top:98px">
  <div class="modhead">
    <h2>Module 1</h2>
    <q>“The story of Navira is the story of determination, courage and ability, it is the story about believing in oneself, in one's own values, and in action rather than stagnation.”</q>
    <cite>-Henrik Lund, Chairman of the Board, June 2014</cite>
  </div>
  <div class="lo">Learning Objectives:</div>
  <div class="locards">
    <div class="loc">Navira Mission,<br>Vision &amp; Values</div>
    <div class="loc">Eight Customer<br>Promises</div>
    <div class="loc">Understanding our<br>Strategic Goals</div>
    <div class="loc">Creating &amp;<br>Communicating<br>Your Vision</div>
    <div class="loc">Introduction to<br>Managerial<br>Leadership</div>
    <div class="loc">Understanding<br>the Role of a<br>Manager</div>
  </div>
  <div class="brand">NAVIRA</div><div class="pg">03</div>
</section>

<!-- 4 exercise 1 -->
<section class="page" style="left:82px;top:567px">
  <div class="tag">Exercise 1</div>
  <div class="sub" style="top:40px;font-size:11px;color:#222">EXPECTATIONS</div>
  <div class="lede" style="top:58px;font-weight:700;font-size:5.6px;color:#333">List the five most important expectations to be considered successful in your role.</div>
  <div class="t1">
    <div class="hd">FIVE MOST IMPORTANT EXPECTATIONS OF MY ROLE</div>
    <div class="r"><div class="n">01</div><div></div></div>
    <div class="r"><div class="n">02</div><div></div></div>
    <div class="r"><div class="n">03</div><div></div></div>
    <div class="r"><div class="n">04</div><div></div></div>
    <div class="r"><div class="n">05</div><div></div></div>
  </div>
  <div class="brand">NAVIRA</div><div class="pg">04</div>
</section>

<!-- 5 exercise 2 -->
<section class="page" style="left:441px;top:567px">
  <div class="tag">Exercise 2</div>
  <div class="sub">Do Our Strategic Goals Align with our Values &amp; Promises?</div>
  <div class="lede" style="top:50px">Review the Strategy Deployment Initiatives and connect them to corresponding Values and Promises. Are there any values or promises that are not aligned to our goals?</div>
  <div class="t2">
    <div class="hd"><div class="e"></div><div>Department</div><div>Level 1 Initiative</div><div>NAVIRA VALUES</div><div>Customer Promises</div></div>
    <div class="r"><div class="n">01</div><div></div><div>Succession Planning</div><div></div><div></div></div>
    <div class="r"><div class="n">02</div><div>HR</div><div>Reach HTNA Saturation of 47%</div><div></div><div></div></div>
    <div class="r"><div class="n">03</div><div></div><div>Increase Technical Competencies of Commercial Team</div><div></div><div></div></div>
    <div class="r"><div class="n">04</div><div>Quality</div><div>Redefine All Processes &amp; Establish Training Schedule</div><div></div><div></div></div>
    <div class="r"><div class="n">05</div><div>EHI</div><div>Improve the Follow up Process of Payment Collection</div><div></div><div></div></div>
    <div class="r"><div class="n">06</div><div></div><div>Market Share of Oil - BFV - HHO - Control Valves</div><div></div><div></div></div>
    <div class="r"><div class="n">07</div><div></div><div>Enhance Project Management</div><div></div><div></div></div>
    <div class="r"><div class="n">08</div><div>Commercial</div><div>Define Service Offer</div><div></div><div></div></div>
    <div class="r"><div class="n">09</div><div></div><div>Enhancing Relationship with Across Departments</div><div></div><div></div></div>
    <div class="r"><div class="n">10</div><div></div><div>Define Sales &amp; Marketing Strategies</div><div></div><div></div></div>
    <div class="r"><div class="n">11</div><div></div><div>Utilize CRM in measuring and Improving Response Time to Customers</div><div></div><div></div></div>
    <div class="r"><div class="n">12</div><div>Supply Chain</div><div>Supply Sustainability</div><div></div><div></div></div>
    <div class="r"><div class="n">13</div><div>Production</div><div>Capacity Improvement</div><div></div><div></div></div>
    <div class="r"><div class="n">14</div><div></div><div>Increase Factory 2 Ability to Produce Larger Size BFV</div><div></div><div></div></div>
  </div>
  <div class="brand">NAVIRA</div><div class="pg">05</div>
</section>

<!-- 6 exercise 3 -->
<section class="page" style="left:795px;top:567px">
  <div class="tag">Exercise 3</div>
  <div class="sub">Reflection Exercise</div>
  <div class="lede" style="top:50px">Reflection is a key part of growth and learning as a leader. Pause to think about what made us successful last year.</div>
  <div class="refl" style="top:68px"><div class="n">01</div><div class="box">What was our most significant accomplishment last year?</div></div>
  <div class="refl w" style="top:124px"><div class="n">02</div><div class="box">How did we get the result?</div></div>
  <div class="refl" style="top:180px"><div class="n">03</div><div class="box">What could we have done better?</div></div>
  <div class="brand">NAVIRA</div><div class="pg">06</div>
</section>

<!-- 7 exercise 4 -->
<section class="page" style="left:82px;top:1035px">
  <div class="tag">Exercise 4</div>
  <div class="sub">Creating Your Vision</div>
  <div class="lede" style="top:49px">Developing and communicating a vision is an important skill for leaders. The following checklists are designed to help you cover the key issues associated with the effective communication of a compelling vision.</div>
  <div class="band" style="top:66px">PART 1 – Identifying Key Components</div>
  <div class="lede" style="top:78px">A vision communicates answers to the basic questions: Who are we, where are we going and why are we going there? For individual leaders the core questions are what do I want to achieve and how will I get there.</div>
  <div class="ex4row" style="top:96px;right:130px"><div class="n">01</div><div class="tiny"><b>A Strong Vision Makes a Case for Change</b>First the vision should justify changing from the status quo. The case for change can be based on many factors such as markets and technology.</div></div>
  <div class="ex4row" style="top:130px;right:130px"><div class="n">02</div><div class="tiny"><b>A Strong Vision Identifies Ideal Strategic Goals</b>Second, ideal goals need to be identified to show how the future will be different from the past. Ideal goals capture a standard of excellence.</div></div>
  <div class="ex4row" style="top:166px;right:130px"><div class="n">03</div><div class="tiny"><b>A Strong Vision Includes a Focus on People</b>Third, the vision needs to recognize the people whose actions are necessary to make the vision a reality.</div></div>
  <div class="ph" style="position:absolute;left:204px;top:96px;width:104px;height:92px" role="img" aria-label="Photo of a conference hall full of seated attendees"></div>
  <div class="band" style="top:196px">PART 2 – Communicating a Vision</div>
  <div class="lede" style="top:208px">Leaders are constantly communicating, everything they say and do as well as how they say and do it, is closely examined by employees. How you act and speak will reinforce your vision.</div>
  <div class="ex4row" style="top:228px;right:130px"><div class="n">01</div><div class="tiny"><b>Heads</b>Strategic communication of the vision develops a clear philosophy connected to the strategic objectives.</div></div>
  <div class="ex4row" style="top:262px;right:130px"><div class="n">02</div><div class="tiny"><b>Hands</b>Tactical release of practices must be aligned with the vision so that people know how to act on it every day.</div></div>
  <div class="ex4row" style="top:300px;right:130px"><div class="n">03</div><div class="tiny"><b>Hearts</b>Generating a feeling of common purpose so people connect personally with the vision and believe in it.</div></div>
  <div class="ph" style="position:absolute;left:204px;top:228px;width:104px;height:102px" role="img" aria-label="Group photo of staff standing outside a company building"></div>
  <div class="brand">NAVIRA</div><div class="pg">07</div>
</section>

<!-- 8 list -->
<section class="page" style="left:441px;top:1035px">
  <div class="listhd">When making suggestions for taking action, I need to...</div>
  <div class="list">
    <div><span class="n">01</span>Explain how my idea fits in with the "big" picture of what we want to accomplish.</div>
    <div><span class="n">02</span>Justify and explain why it would be the right thing to do.</div>
    <div><span class="n">03</span>Emphasize the rational arguments for taking that action.</div>
    <div><span class="n">04</span>Try to connect the needs &amp; interests of others to the action.</div>
    <div><span class="n">05</span>Talk in terms of what we would ideally like to accomplish.</div>
    <div><span class="n">06</span>Try to make my suggestion as vivid as possible.</div>
    <div><span class="n">07</span>Offer examples of how my approach will make a difference to people.</div>
    <div><span class="n">08</span>Avoid getting into too many details until people have agreed to my basic idea.</div>
    <div><span class="n">09</span>Try to explain how my suggestion will benefit us in the future.</div>
    <div><span class="n">10</span>Look for ways to connect what I want to do with what others want to do.</div>
  </div>
  <div style="position:absolute;left:0;right:0;top:232px;height:195px;background:linear-gradient(180deg,#fff 0%,#b8bfe3 30%,#7d88c6 70%,#fff 100%)" role="img" aria-label="Photo of a speaker presenting at a podium, faded into the page in blue"></div>
  <div class="brand">NAVIRA</div><div class="pg">08</div>
</section>

<!-- 9 exercise 5 -->
<section class="page" style="left:795px;top:1035px">
  <div class="tag">Exercise 5</div>
  <div class="sub">Communicating Your Vision</div>
  <div class="lede" style="top:50px">Describe your goal below and then list the tasks the team needs to accomplish to meet the goal. Determine who is responsible for the task and describe in detail what it will look like when it is complete.</div>
  <div class="lede" style="top:68px;font-style:italic">Performance Goal: <span style="display:inline-block;width:200px;border-bottom:1px solid #999"></span></div>
  <div class="t5">
    <div class="hd"><div class="e"></div><div>Task</div><div>Responsible</div><div>What does success look like?</div></div>
    <div class="r"><div class="n">01</div><div></div><div></div><div></div></div>
    <div class="r"><div class="n">02</div><div></div><div></div><div></div></div>
    <div class="r"><div class="n">03</div><div></div><div></div><div></div></div>
    <div class="r"><div class="n">04</div><div></div><div></div><div></div></div>
    <div class="r"><div class="n">05</div><div></div><div></div><div></div></div>
    <div class="r"><div class="n">06</div><div></div><div></div><div></div></div>
  </div>
  <div class="brand">NAVIRA</div><div class="pg">09</div>
</section>

<!-- 10 exercise 6 -->
<section class="page" style="left:82px;top:1504px">
  <div class="tag">Exercise 6</div>
  <div class="sub">Delegating Effectively</div>
  <div class="lede" style="top:50px">After identifying the goals in detail and outlining what will be required to achieve them, use the checklist below to ensure that you delegate every aspect. This will help you communicate the goal clearly and ensure the responsible person has authority.</div>
  <div class="steps">
    <div class="hd">5 Steps to Effective Delegation</div>
    <div class="step"><div class="n">01</div><div><strong>Clarity –</strong>In your own mind, decide what it is you want done and why. It is an appropriate assignment for the individual. Make sure the person has the proper authority to carry out the task and obtain the resources to complete it.</div></div>
    <div class="step"><div class="n">02</div><div><strong>Explain –</strong>Meet with the employee and discuss the assignment and your expectations. Make sure the employee understands how the task relates to organizational goals and how you will appraise and monitor. Ensure the deadlines and milestones are clear by asking the employee questions to repeat his understanding of the task.</div></div>
    <div class="step"><div class="n">03</div><div><strong>Let Go –</strong>Allow the employee to do the task how they feel comfortable. Show trust in their abilities and offer encouragement.</div></div>
    <div class="step"><div class="n">04</div><div><strong>Check In –</strong>Periodically check on the progress of the assignment but do not rush to the rescue at the first sign that things are off track. The employee may have felt that the assignment was beyond their capabilities and may be embarrassed to raise any issues. Allow them time to solve the problem. At the start you can explicitly tell the employee you are confident in their abilities and understand that this is a challenging task so you are ready to help. Let them know that you expect them to find solutions and come to you with any questions.</div></div>
    <div class="step"><div class="n">05</div><div><strong>Acknowledge –</strong>Recognize their accomplishments and show appreciation upon completing the work. Make sure the employee recognizes what they accomplished and how it contributed to the work's functioning and their development.</div></div>
  </div>
  <div class="brand">NAVIRA</div><div class="pg">10</div>
</section>

<!-- 11 leadership styles -->
<section class="page" style="left:441px;top:1504px">
  <div class="title" style="font-size:10px">Overview of Leadership Styles</div>
  <div class="lede" style="top:42px;font-size:5.4px;color:#444">“Before you are a leader, success is all about growing yourself. When you become a leader, success is all about growing others.”<br>— Martin Hale, former CEO of Northwind Industries</div>
  <div class="t11">
    <div class="hd"><div>TERM</div><div>DEFINITION</div><div>OUTCOME</div></div>
    <div class="r"><div class="term">AUTOCRATIC</div><div>A leadership style that is boss-centered and authoritarian</div><div>Produces short term productivity but in the long run it reduces responsibility as employees delegate upwards</div></div>
    <div class="r"><div class="term">CHARISMATIC</div><div>A leadership style in which the leader uses the power of their influence and appeal, as well as inspiration and empowerment, to achieve change</div><div>Useful for short term initiatives that require selling a new idea &amp; fostering adoption</div></div>
    <div class="r"><div class="term">DEMOCRATIC</div><div>A leadership style in which the leader relies heavily on input from others, especially if they are impacted by the decisions being made</div><div>Creates consistency in results as employees feel involved in decision making</div></div>
    <div class="r"><div class="term">LAISSEZ-FAIRE</div><div>Translates to "let do" or "let them do it," which reflects a leadership style that is very hands-off and a belief that the subordinates will self-regulate</div><div>Effective for teams of experts who do not require hands-on management</div></div>
    <div class="r"><div class="term">SERVANT LEADER</div><div>A leadership style in which the leader consistently looks for better ways to provide and support followers</div><div>Employees are highly productive and engaged because manager acts to remove obstacles and supports them to achieve goals</div></div>
    <div class="r"><div class="term">SITUATIONAL LEADERSHIP MODEL</div><div>Focuses on the belief that no one leadership style works best in all cases and that the leader needs to adapt to fit the situation</div><div>Difficult to execute as it requires leader to be skilled in many styles</div></div>
  </div>
  <div class="brand">NAVIRA</div><div class="pg">11</div>
</section>

<!-- 12 scenario -->
<section class="page" style="left:795px;top:1504px">
  <div class="title" style="font-size:8px">Real Life Scenario - Leadership Values in Action</div>
  <div class="art" style="top:52px;font:700 7px 'Roboto Condensed',sans-serif;color:var(--navy)">Marlow Human Resources Conference<br>By Peter Olsen, CEO</div>
  <div class="art tiny" style="top:72px;font-size:3.6px">May 8, 1996</div>
  <div class="art tiny" style="top:82px;font-size:3.6px">As we look ahead, we realize that the most fundamental psychological and emotional need of our people is to be respected, to feel they belong and to know that their work matters. Leaders who understand this build organizations where people choose to give their best effort every single day. When people feel valued they bring energy, ideas and loyalty, and they share in the success of the whole team. We must remember that our results are created by people, and that the way we lead determines how much of their talent we actually use.<br><br>What is achieved if it is how a person feels about himself. It is not just about being recognised but about knowing that the work makes a real difference to customers and colleagues alike.<br><br>Remember, a happy employee is more productive, more loyal and more willing to go the extra mile for our customers and partners.</div>
  <div class="art" style="top:202px;font:700 5px Arimo,sans-serif;color:var(--blue)">So, how we treat our people becomes one of our most important management objectives:</div>
  <div class="art bul" style="top:212px">
    <div>People like to feel that they belong</div>
    <div>People like to feel that they are being involved</div>
    <div>People like to feel that they are part of something important</div>
    <div>People like to feel that others listen to what they have to say</div>
    <div>People like to be recognized for their accomplishments</div>
    <div>People like to be part of a successful team</div>
    <div>People like to be proud of a company that is proud of them</div>
  </div>
  <div class="art tiny" style="top:318px;font-size:3.6px">We all know that we can be there for all of our people and it doesn't cost a fortune. However, the return on your investment is significant, and remember that the way we treat our people will always show in results.</div>
  <div class="art" style="top:340px;font:700 6.5px 'Roboto Condensed',sans-serif;color:var(--blue)">In every situation - always do what is right.</div>
  <div class="brand">NAVIRA</div><div class="pg">12</div>
</section>

<!-- 13 competing values -->
<section class="page" style="left:82px;top:1974px">
  <div class="qtitle">THE COMPETING VALUES FRAMEWORK DESCRIPTION</div>
  <div class="axis" style="left:0;right:0;top:56px;text-align:center">Flexibility &amp; Discretion</div>
  <div class="axis" style="left:0;right:0;top:348px;text-align:center">Stability &amp; Control</div>
  <div class="axis" style="left:26px;top:208px;transform:translate(-50%,-50%) rotate(-90deg)">Internal Focus &amp; Integration</div>
  <div class="axis" style="left:302px;top:208px;transform:translate(-50%,-50%) rotate(90deg)">External Focus &amp; Differentiation</div>
  <div class="quad">
    <div class="q"><h4>Culture Type: Collaborate</h4><p class="k">Leader Type:<br>Facilitator, Mentor &amp; Team Builder</p><p>Value Drivers:<br>Commitment, Communication, Development</p><p>Theory of Effectiveness:<br>Human development and participation produce effectiveness</p><p>Quality Drivers:<br>Employee involvement, open communication &amp; empowerment</p></div>
    <div class="q"><h4>Culture Type: Create</h4><p class="k">Leader Type:<br>Innovator, Entrepreneur, Visionary</p><p>Value Drivers:<br>Innovative outputs, transformation and agility</p><p>Theory of Effectiveness:<br>Innovation &amp; new resources produce effectiveness</p><p>Quality Drivers:<br>Continuous improvement, surprise &amp; delight, creating new standards</p></div>
    <div class="q"><h4>Culture Type: Control</h4><p class="k">Leader Type:<br>Coordinator, Monitor, Organizer</p><p>Value Drivers:<br>Efficiency, Timeliness, Consistency &amp; Uniformity</p><p>Theory of Effectiveness:<br>Control and efficiency with capable processes produce effectiveness</p><p>Quality Drivers:<br>Error detection, process control, systematic problem solving</p></div>
    <div class="q"><h4>Culture Type: Compete</h4><p class="k">Leader Type:<br>Hard driver, Competitor, Doer</p><p>Value Drivers:<br>Goal achievement, profitability, and market share</p><p>Theory of Effectiveness:<br>Aggressively competing and customer focus produce effectiveness</p><p>Quality Drivers:<br>Measuring customer preferences, improving productivity, partnerships</p></div>
  </div>
  <div class="brand">NAVIRA</div><div class="pg">13</div>
</section>

<!-- 14 manager responsibilities -->
<section class="page" style="left:441px;top:1974px">
  <div class="qtitle" style="top:20px">THE CRITICAL MANAGER RESPONSIBILITIES</div>
  <div class="axis" style="left:0;right:0;top:56px;text-align:center">Flexibility &amp; Discretion</div>
  <div class="axis" style="left:0;right:0;top:348px;text-align:center">Stability &amp; Control</div>
  <div class="axis" style="left:26px;top:208px;transform:translate(-50%,-50%) rotate(-90deg)">Internal Focus &amp; Integration</div>
  <div class="axis" style="left:302px;top:208px;transform:translate(-50%,-50%) rotate(90deg)">External Focus &amp; Differentiation</div>
  <div class="quad">
    <div class="q"><h4>Collaborate Skills</h4><p>Manage Teams</p><p class="k">Facilitate high-performance teamwork</p><p>Manage Relationships</p><p class="k">Listen, support and give feedback</p><p>Theory of Effectiveness</p><p class="k">Human development and participation</p><p>Develop Others</p><p class="k">Help people improve performance</p></div>
    <div class="q"><h4>Create Skills</h4><p>Manage Innovation</p><p class="k">Encourage creativity, facilitate new ideas</p><p>Manage the Future</p><p class="k">Communicate a clear vision for the future</p><p>Manage Continuous Improvement</p><p class="k">Foster flexibility and productive change</p></div>
    <div class="q"><h4>Control Skills</h4><p>Manage the Culture</p><p class="k">Help people understand what is expected of them</p><p>Manage the System</p><p class="k">Ensure that procedures and measurements are in place</p><p>Manage Coordination</p><p class="k">Foster information sharing across units</p></div>
    <div class="q"><h4>Compete Skills</h4><p>Manage Competitiveness</p><p class="k">Foster an orientation towards exceeding competitors</p><p>Energize Employees</p><p class="k">Motivate and inspire people to be proactive</p><p>Manage Customer Service</p><p class="k">Foster a focus on serving customers</p></div>
  </div>
  <div class="brand">NAVIRA</div><div class="pg">14</div>
</section>

<!-- 15 radar -->
<section class="page" style="left:795px;top:1974px">
  <div class="title" style="font-size:8px">Introduction to Managerial Leadership</div>
  <div class="lede" style="top:40px;font-size:4.8px">Understanding your organization's culture and your leadership styles will help you know what influences employee behaviors and outcomes. Then you need to decide what is working and what needs to change.</div>
  <div style="position:absolute;left:22px;right:22px;top:66px;height:270px;border:1px solid #9fb0d6"></div>
  <svg style="position:absolute;left:22px;top:66px" width="284" height="270" viewBox="0 0 284 270" aria-label="Radar chart of current and future organizational culture">
    <text x="142" y="12" text-anchor="middle" font-size="5" fill="#0054AA" font-family="Arimo">Representation of NVC Organizational Culture</text>
    <text x="142" y="22" text-anchor="middle" font-size="4.4" font-weight="700" fill="#333" font-family="Arimo">Flexibility &amp; Discretion</text>
    <text x="142" y="252" text-anchor="middle" font-size="4.4" font-weight="700" fill="#333" font-family="Arimo">Stability &amp; Control</text>
    <text transform="translate(12 137) rotate(-90)" text-anchor="middle" font-size="4" font-weight="700" fill="#333" font-family="Arimo">Internal Focus &amp; Integration</text>
    <text transform="translate(272 137) rotate(90)" text-anchor="middle" font-size="4" font-weight="700" fill="#333" font-family="Arimo">External Focus &amp; Differentiation</text>
    <g font-family="Arimo" font-size="12" font-weight="700" fill="#d8deeb">
      <text x="50" y="45">Collaborate</text><text x="178" y="45">Create</text>
      <text x="50" y="225">Control</text><text x="178" y="225">Compete</text>
    </g>
    <line x1="40" y1="30" x2="244" y2="240" stroke="#333" stroke-width=".6"/>
    <line x1="244" y1="30" x2="40" y2="240" stroke="#333" stroke-width=".6"/>
    <g font-size="4.5" fill="#333" font-family="Arimo"><text x="152" y="118">20</text><text x="196" y="80">40</text><text x="226" y="50">50</text></g>
    <polygon points="100,84 154,126 164,176 70,200" fill="none" stroke="#333" stroke-width="1.2"/>
    <polygon points="110,96 200,78 170,170 108,172" fill="none" stroke="#333" stroke-width=".8" stroke-dasharray="2 1.5"/>
    <line x1="168" y1="210" x2="184" y2="210" stroke="#333" stroke-width="1.2"/>
    <text x="188" y="212" font-size="4.4" font-weight="700" font-family="Arimo" fill="#333">Current State</text>
    <line x1="168" y1="218" x2="184" y2="218" stroke="#333" stroke-width=".8" stroke-dasharray="2 1.5"/>
    <text x="188" y="220" font-size="4.4" font-weight="700" font-family="Arimo" fill="#333">Future State</text>
  </svg>
  <div class="brand">NAVIRA</div><div class="pg">15</div>
</section>

<!-- 16 back cover -->
<section class="page back" style="left:264px;top:2442px">
  <div style="position:absolute;left:0;right:0;top:0;height:300px;background:linear-gradient(180deg,rgba(255,255,255,.08),rgba(255,255,255,0))" role="img" aria-label="Faint blue-tinted photo of a meeting room with a conference table"></div>
  <div class="house"></div>
  <div class="hm" style="bottom:66px;font-size:24px">NAVIRA</div>
  <div class="hm" style="bottom:14px;font-size:15px;line-height:1.05">LEADERSHIP<br>DEVELOPMENT</div>
</section>

<!-- 17 exercise 2 blank -->
<section class="page" style="left:628px;top:2442px">
  <div class="tag">Exercise 2</div>
  <div class="sub">Do Our Strategic Goals Align with our Values &amp; Promises?</div>
  <div class="lede" style="top:50px">Review the Strategy Deployment Initiatives and connect them to corresponding Values and Promises. Are there any values or promises that are not aligned to our goals?</div>
  <div class="t2">
    <div class="hd"><div class="e"></div><div>Department</div><div>Level 1 Initiative</div><div>NAVIRA VALUES</div><div>Customer Promises</div></div>
    <div class="r"><div class="n">01</div><div></div><div></div><div></div><div></div></div>
    <div class="r"><div class="n">02</div><div></div><div></div><div></div><div></div></div>
    <div class="r"><div class="n">03</div><div></div><div></div><div></div><div></div></div>
    <div class="r"><div class="n">04</div><div></div><div></div><div></div><div></div></div>
    <div class="r"><div class="n">05</div><div></div><div></div><div></div><div></div></div>
    <div class="r"><div class="n">06</div><div></div><div></div><div></div><div></div></div>
    <div class="r"><div class="n">07</div><div></div><div></div><div></div><div></div></div>
    <div class="r"><div class="n">08</div><div></div><div></div><div></div><div></div></div>
    <div class="r"><div class="n">09</div><div></div><div></div><div></div><div></div></div>
    <div class="r"><div class="n">10</div><div></div><div></div><div></div><div></div></div>
    <div class="r"><div class="n">11</div><div></div><div></div><div></div><div></div></div>
    <div class="r"><div class="n">12</div><div></div><div></div><div></div><div></div></div>
    <div class="r"><div class="n">13</div><div></div><div></div><div></div><div></div></div>
    <div class="r"><div class="n">14</div><div></div><div></div><div></div><div></div></div>
  </div>
  <div class="brand">NAVIRA</div><div class="pg">05</div>
</section>

</div>
</body>
</html>
```